Grafik/Logo für ein Schulungszertifikat DIN A4
Zielgruppe
Es soll nach einer Schulung für Social Media und Online Marketing für Unternehmer und Selbstständige ein Zertifikat auf dickerem Papier ausgehändigt werden.
Auf dieses sollen die Teilnehmer stolz sein ;-) und im Büro oder im Geschäft aufhängen wollen.
Das Logo des Zertifikates darf anschließend auch alleinstehend auf der Homepage der Unternehmensseiten von Teilnehmern verwendet werden dürfen.
Es soll eine Gemeinschaft symbolisiert werden. Denn bei dieser Schulung schulen Unternehmer aus dem Bereich Onlinemarketing andere Unternehmer aus unterschiedlichsten Branchen und Bereichen. Eben aus allen, in denen Onlinemarketing und Social Media sinnvoll eingesetzt werden kann.
Die Inhalte können Sie dem beigefügten Dokument entnehmen.
Aufgabenstellung
Es werden benötigt:
1. Ein Logo/Zertifikatssiegel (auffälig sein und ins Auge fallen, ob online oder wenn das an der Wand hängt, oder als Autoaufkleber genutzt wird)
2. Layout für das DIN A 4 Zertifikat mit dem Zertifikatssiegel

```html
<!DOCTYPE html>
<html lang="de">
<head>
<meta charset="utf-8">
<title>Zertifikat – Social Media und Online Marketing</title>
<link rel="stylesheet" href="https://fonts.googleapis.com/css2?family=Fira+Sans:wght@400;500;700&display=swap">
<style>
  :root {
    --teal: #3a9aa6;
    --teal-dark: #216f78;
    --teal-deep: #1a5d66;
    --red: #d21f2b;
    --orange: #ec6a3b;
    --text: #4a4a4a;
    --text-dark: #2e2e2e;
    --white: #ffffff;
    --paper: #ffffff;
  }
  * { margin: 0; padding: 0; box-sizing: border-box; }
  html, body { width: 849px; height: 1200px; overflow: hidden; background: var(--paper); }
  body { font-family: "Fira Sans", Arial, sans-serif; color: var(--text); }
  .certificate { position: relative; width: 849px; height: 1200px; background: var(--paper); overflow: hidden; }

  .accent-strip {
    position: absolute; left: 0; width: 100%; height: 12px;
    background: linear-gradient(90deg, var(--red) 0%, var(--orange) 50%, var(--red) 100%);
  }
  .accent-strip--top { top: 0; }
  .accent-strip--bottom { top: 1160px; height: 18px; }

  .header { position: absolute; top: 12px; left: 0; width: 100%; height: 318px; background: var(--teal); }
  .brand { position: absolute; top: 20px; left: 0; width: 100%; text-align: center; color: var(--white); }
  .brand__name { font-size: 50px; font-weight: 400; line-height: 1; letter-spacing: -1px; }
  .brand__tagline { margin-top: 42px; font-size: 15px; font-weight: 400; }
  .header__title {
    position: absolute; top: 190px; left: 0; width: 100%; text-align: center;
    color: var(--white); font-size: 100px; font-weight: 500; letter-spacing: 12px; line-height: 1;
  }
  .header-band {
    position: absolute; top: 330px; left: 0; width: 100%; height: 47px;
    border-top: 3px solid #cfe6e9;
    background: linear-gradient(90deg, var(--teal-deep) 0%, var(--teal) 50%, var(--teal-deep) 100%);
  }

  .recipient { position: absolute; top: 420px; left: 0; width: 100%; text-align: center; font-size: 43px; font-weight: 500; color: var(--text); }
  .period { position: absolute; top: 514px; left: 0; width: 100%; text-align: center; font-size: 18px; line-height: 25px; }
  .period strong { font-weight: 700; color: var(--text-dark); }
  .seminar-intro { position: absolute; top: 585px; left: 0; width: 100%; text-align: center; font-size: 18px; }
  .seminar-title { position: absolute; top: 617px; left: 0; width: 100%; text-align: center; font-size: 36px; font-weight: 500; }
  .statement { position: absolute; top: 680px; left: 124px; width: 600px; font-size: 19px; line-height: 29px; color: var(--text-dark); }
  .place-date { position: absolute; top: 825px; left: 124px; font-size: 19px; }

  .signature { position: absolute; top: 896px; }
  .signature--ceo { left: 124px; }
  .signature--lead { left: 339px; }
  .signature__name { font-size: 19px; }
  .signature__role { margin-top: 7px; font-size: 10px; font-weight: 500; color: var(--text-dark); }

  .topics { position: absolute; top: 1002px; left: 124px; font-size: 10px; line-height: 13.4px; font-weight: 500; color: var(--text-dark); list-style: none; }
  .topics__heading { font-weight: 700; }

  .seal { position: absolute; left: 552px; top: 884px; width: 270px; height: 270px; }
</style>
</head>
<body>
<main class="certificate">
  <div class="accent-strip accent-strip--top"></div>

  <header class="header">
    <div class="brand">
      <div class="brand__name">Brightwave</div>
      <div class="brand__tagline">Kommunikationsagentur • Social Media</div>
    </div>
    <h1 class="header__title">ZERTIFIKAT</h1>
  </header>
  <div class="header-band"></div>

  <p class="recipient">Vorname Nachname</p>
  <p class="period">hat in der Zeit von<br><strong>1. November bis 23. Dezember 2014</strong></p>
  <p class="seminar-intro">das Seminar</p>
  <h2 class="seminar-title">Social Media und Online Marketing</h2>
  <p class="statement">absolviert und neben fachlicher Kompetenz auch die praxisgerechte Umsetzung im Rahmen einer Abschlussprüfung erfolgreich nachgewie-sen.</p>

  <p class="place-date">Dortmund, den 8. Januar 2015</p>

  <div class="signature signature--ceo">
    <div class="signature__name">Lena Hartwig</div>
    <div class="signature__role">Geschäftsführerin</div>
  </div>
  <div class="signature signature--lead">
    <div class="signature__name">Vorname Nachname</div>
    <div class="signature__role">Lehrgangsleiter</div>
  </div>

  <ul class="topics">
    <li class="topics__heading">Themenschwerpunkte:</li>
    <li>Die Website: „Das Herz im Social Business“</li>
    <li>Suchmaschinenoptimierung und Linkbuilding</li>
    <li>Blog und Blogredaktion</li>
    <li>Internetrecht/ Social Media-Recht</li>
    <li>Socialbook – Grundlagen und Einbindung in Kommunikationsstrategien</li>
    <li>Bizlink</li>
    <li>Chirper und Searchly+</li>
    <li>Monitoring</li>
    <li>Searchly Ads, Searchly Dienste und Searchly Analytics</li>
  </ul>

  <svg class="seal" viewBox="0 0 270 270" role="img" aria-label="Zertifikatssiegel der Weiterbildung">
    <circle cx="135" cy="135" r="133" fill="#d9eef1"/>
    <circle cx="135" cy="135" r="122" fill="var(--teal)"/>
    <circle cx="135" cy="135" r="88" fill="#ffffff"/>
    <circle cx="135" cy="135" r="80" fill="#cfe6e9"/>
  </svg>

  <div class="accent-strip accent-strip--bottom"></div>
</main>
</body>
</html>
```